Local Swedish accounting firm needs a webpage design.

We need a logo design for an accounting firm based in Malmö, Sweden called "Veltrano". We provide a full range of accounting services and have worked closely with startups for many years.
We would like to see an design using the following color scheme.
https://tintboard.example/4a7c2e-e1d093-8f3b6a-19c4d7-b2560f
The design should communicate ease of use and financial safety.

Target Market(s)

We are an accounting firm so are clients are startups and small to medium sized companys

Industry/Entity Type

Accounting

Coding

Coded - Design and coding required

Number of Pages Required

1 page

Font styles to use
Sans Serif

```html
<!DOCTYPE html>
<html lang="en">
<head>
<meta charset="utf-8">
<title>Veltrano – Accounting in Malmö</title>
<link rel="stylesheet" href="https://fonts.googleapis.com/css2?family=Open+Sans:wght@400;600;700&display=swap">
<style>
:root{
  --brand:#4a7c2e;
  --brand-dark:#3f6a27;
  --sand:#e1d093;
  --plum:#8f3b6a;
  --cyan:#19c4d7;
  --rust:#b2560f;
  --ink:#2d3748;
  --text:#4a4f5a;
  --muted-bg:#f5f3ea;
  --blob:#faf8ef;
  --on-brand:#eef5e8;
  --white:#ffffff;
}
*{box-sizing:border-box;margin:0;padding:0}
html,body{width:1200px;height:2500px;overflow:hidden}
body{font-family:"Open Sans",sans-serif;color:var(--text);background:var(--white);position:relative}
.abs{position:absolute}
a{text-decoration:none;color:inherit}

.top-strip{left:0;top:0;width:1200px;height:7px;background:var(--brand)}
.site-header{left:0;top:7px;width:1200px;height:71px;background:var(--white);box-shadow:0 2px 6px rgba(0,0,0,.05)}
.wordmark{left:39px;top:16px;font-size:32px;font-weight:400;color:#111;letter-spacing:-.5px}
.main-nav{left:402px;top:26px;display:flex;gap:27px;font-size:14px;color:#333}
.btn-login{left:1008px;top:15px;width:147px;height:39px;border-radius:20px;background:var(--brand);color:var(--white);font-size:14px;font-weight:700;display:flex;align-items:center;justify-content:center}

.hero-title{left:88px;top:184px;font-size:39px;line-height:52px;font-weight:700;color:var(--brand)}
.hero-lead{left:88px;top:312px;width:450px;font-size:19px;line-height:26px;color:#555}
.btn-solid{background:var(--brand);color:var(--white);border-radius:20px;font-size:14px;font-weight:700;display:flex;align-items:center;justify-content:center}
.hero-cta{left:88px;top:438px;width:147px;height:40px}
.hero-art{left:600px;top:135px;width:575px;height:430px}

.booking-band{left:0;top:592px;width:1200px;height:91px;background:var(--brand)}
.booking-text{left:203px;top:28px;font-size:19px;font-weight:700;color:var(--white)}
.btn-ghost-light{left:840px;top:26px;width:128px;height:39px;border:1.5px solid var(--white);border-radius:20px;color:var(--white);font-size:14px;font-weight:700;display:flex;align-items:center;justify-content:center}

.intro{left:0;top:683px;width:1200px;height:373px;background:var(--muted-bg)}
.intro-title{left:0;top:728px;width:1200px;text-align:center;font-size:32px;line-height:43px;font-weight:700;color:var(--ink)}
.intro-title span{color:var(--plum)}
.intro-lead{left:290px;top:836px;width:650px;text-align:center;font-size:19px;line-height:26px;color:#555}
.btn-outline{border:1.5px solid var(--brand);border-radius:20px;color:var(--brand);font-size:14px;font-weight:700;display:flex;align-items:center;justify-content:center;background:transparent}
.intro-cta{left:541px;top:951px;width:147px;height:39px}

.services-blob{left:0;top:1070px;width:610px;height:930px}
.services-title{left:0;top:1094px;width:1170px;text-align:center;font-size:32px;font-weight:700;color:var(--ink)}
.services-lead{left:265px;top:1155px;width:650px;text-align:center;font-size:19px;line-height:26px;color:#555}
.services-cta{left:503px;top:1230px;width:147px;height:39px}

.service-icon{width:66px;height:66px}
.service-title{font-size:23px;font-weight:600;color:var(--ink)}
.service-text{font-size:16px;line-height:28.2px;color:#555;white-space:nowrap}
.read-more{font-size:19px;font-weight:600;color:var(--brand);border-bottom:2px solid var(--brand);padding-bottom:6px;width:113px}

.site-footer{left:0;top:2115px;width:1200px;height:330px;background:var(--brand)}
.footer-logo{left:141px;top:2155px;width:115px;height:72px;background:var(--white);display:flex;align-items:center;justify-content:center;gap:6px;font-size:14px;color:#333}
.footer-logo i{display:block;width:10px;height:10px;background:var(--rust)}
.footer-contact{left:139px;top:2244px;font-size:16px;line-height:28.8px;color:var(--on-brand);font-style:normal}
.footer-col{font-size:16px;line-height:28.8px;color:var(--on-brand)}
.footer-col h4{font-size:16px;font-weight:700;color:var(--white)}
.member{left:932px;top:2149px;width:220px;font-size:16px;line-height:22px;color:var(--on-brand)}
.member-badge{left:932px;top:2238px;width:90px;height:54px;border-radius:6px;background:var(--sand)}
.footer-bottom{left:0;top:2445px;width:1200px;height:48px;background:var(--brand-dark);border-top:1px solid rgba(255,255,255,.15)}
.copyright{left:133px;top:2460px;font-size:12px;color:var(--on-brand)}
.legal{left:915px;top:2458px;font-size:11px;color:var(--on-brand)}
.accent-strip{left:0;top:2493px;width:1200px;height:7px;background:var(--rust)}
</style>
</head>
<body>

<div class="abs top-strip"></div>
<header class="abs site-header">
  <div class="abs wordmark">VELTRANO</div>
  <nav class="abs main-nav">
    <a>Startsida</a><a>Våra tjänster</a><a>Om Veltrano</a><a>För entreprenörer</a><a>GDPR</a><a>Kontakt</a>
  </nav>
  <a class="abs btn-login">Kundinloggning</a>
</header>

<section>
  <h1 class="abs hero-title">We Are More<br>Than Just Accountants</h1>
  <p class="abs hero-lead">Lorem ipsum dolor sit amet, consectetur<br>adipiscing elit, sed do eiusmod tempor incididunt<br>ut labore et dolore magna aliqua. Ut enim ad</p>
  <a class="abs btn-solid hero-cta">Contact Us</a>
  <svg class="abs hero-art" viewBox="0 0 575 430" role="img" aria-label="Illustration of a calculator, a laptop showing pie and bar charts, and stacks of gold coins">
    <defs>
      <linearGradient id="heroGrad" x1="0" y1="0" x2="1" y2="1">
        <stop offset="0" stop-color="#eef6f7"/>
        <stop offset=".45" stop-color="#bfe9ee"/>
        <stop offset=".75" stop-color="#19c4d7"/>
        <stop offset="1" stop-color="#e1d093"/>
      </linearGradient>
    </defs>
    <path d="M190 60 C200 0 280 -10 340 30 C400 70 470 30 530 80 C590 140 560 230 560 300 C560 380 540 430 460 430 L60 430 C10 430 0 380 20 330 C40 280 30 220 60 170 C90 120 180 120 190 60 Z" fill="url(#heroGrad)"/>
  </svg>
</section>

<section class="abs booking-band">
  <p class="abs booking-text">Book a 1 hour appointment to discuss your business needs</p>
  <a class="abs btn-ghost-light">Book Now</a>
</section>

<section class="abs intro"></section>
<h2 class="abs intro-title">We are <span>Veltrano</span>, and we are here to<br>help saving your time and money.</h2>
<p class="abs intro-lead">Lorem ipsum dolor sit amet, consectetur adipiscing elit, sed do eiusmod tempor incididunt ut labore et dolore magna aliqua. Ut enim ad minim veniam, quis nostrud exercitation ullamco.</p>
<a class="abs btn-outline intro-cta">About Us</a>

<svg class="abs services-blob" viewBox="0 0 610 930" aria-hidden="true">
  <path d="M0 60 C60 20 150 0 210 60 C280 130 290 240 380 270 C480 300 600 300 600 420 C600 560 540 600 560 720 C580 860 420 930 300 925 C180 920 80 870 0 900 Z" fill="var(--blob)"/>
</svg>
<h2 class="abs services-title">Our Services</h2>
<p class="abs services-lead">Lorem ipsum dolor sit amet, consectetur adipiscing elit, sed do eiusmod tempor incididunt ut labore et dolore magna aliqua.</p>
<a class="abs btn-outline services-cta">View All Services</a>

<svg class="abs service-icon" style="left:110px;top:1325px" viewBox="0 0 66 66" fill="none" stroke="var(--brand)" stroke-width="3" stroke-linecap="round">
  <rect x="5" y="3" width="56" height="62" rx="6"/>
  <path d="M22 12 v22 M28 16 c-2-3-12-3-12 2 s12 3 12 8 s-10 5-12 2"/>
  <path d="M36 18 h14 M36 26 h14 M16 42 h34 M16 50 h34"/>
</svg>
<h3 class="abs service-title" style="left:200px;top:1317px">Accounting</h3>
<p class="abs service-text" style="left:200px;top:1355px">Om du vill ägna dig helhjärtat åt din<br>affärsverksamhet är hjälp med den löpande<br>redovisningen ett gott råd. Då behöver du<br>inte lägga tid på vare sig administration,<br>redovisning eller att hålla dig uppdaterad om<br>regel-förändringar. Det gör vi åt dig.</p>
<a class="abs read-more" style="left:200px;top:1548px">Read more</a>

<svg class="abs service-icon" style="left:617px;top:1316px" viewBox="0 0 66 66" fill="none" stroke="var(--brand)" stroke-width="3.2" stroke-linecap="round">
  <circle cx="33" cy="29" r="26"/>
  <path d="M33 14 v30 M41 20 c-3-4-16-4-16 3 s16 4 16 11 s-13 6-16 2"/>
  <path d="M12 62 h42"/>
</svg>
<h3 class="abs service-title" style="left:705px;top:1317px">Payroll management</h3>
<p class="abs service-text" style="left:705px;top:1355px">En genomtänkt grundstruktur för rutiner,<br>redovisning och datainformation frigör mängder<br>med tid. Värdefull tid som kan användas på ett<br>mer lönsamt sätt i företaget. Vi kan hjälpa dig att<br>förbättra företagets rutiner. Vi skapar en stabil<br>grundstruktur för ett effektivt ekonomiflöde.</p>
<a class="abs read-more" style="left:705px;top:1548px;width:118px">Read more</a>

<svg class="abs service-icon" style="left:107px;top:1650px" viewBox="0 0 66 66" fill="none" stroke="var(--brand)" stroke-width="3" stroke-linejoin="round" stroke-linecap="round">
  <path d="M60 4 C40 4 26 14 18 32 L32 46 C50 38 60 24 60 4 Z"/>
  <circle cx="42" cy="22" r="5"/>
  <path d="M18 32 L6 30 L16 20 L28 20 M32 46 L34 58 L44 48 L44 38 M14 44 L6 58 L20 52"/>
</svg>
<h3 class="abs service-title" style="left:196px;top:1647px">Project accounting</h3>
<p class="abs service-text" style="left:196px;top:1685px">Ekonomisk information svart på vitt är oftast<br>bästa beslutsunderlaget. Beslut baserade på<br>antaganden håller sällan i längden. Säkra och<br>tydliga beslutsunderlag ger dig möjlighet att<br>förutse effekterna av olika<br>handlingsalternativ och utveckla företaget i<br>rätt riktning.</p>
<a class="abs read-more" style="left:196px;top:1904px">Read more</a>

<svg class="abs service-icon" style="left:611px;top:1647px" viewBox="0 0 66 66" fill="none" stroke="var(--brand)" stroke-width="3" stroke-linejoin="round" stroke-linecap="round">
  <path d="M22 22 H8 a4 4 0 0 0-4 4 V58 a4 4 0 0 0 4 4 H58 a4 4 0 0 0 4-4 V34"/>
  <path d="M52 4 l10 10 L34 42 l-14 4 l4-14 Z M46 10 l10 10"/>
  <path d="M14 54 h38"/>
</svg>
<h3 class="abs service-title" style="left:701px;top:1647px">Financial management</h3>
<p class="abs service-text" style="left:701px;top:1685px">Som din externa ekonomiavdelning tillför vi<br>ekonomisk kompetens inom<br>alla områden och tar ett helhetsansvar för<br>ekonomifunktionen. Du får någon som hjälper dig<br>att ha kontroll över den operativa verksamheten,<br>som reagerar och ger goda råd på vägen.</p>
<a class="abs read-more" style="left:701px;top:1877px;width:118px">Read more</a>

<footer class="abs site-footer"></footer>
<div class="abs footer-logo"><i></i>VELTRANO</div>
<address class="abs footer-contact">
  Lindholmsgatan 12<br>211 45 Malmö<br><br>Tel:&nbsp; 040-55 12 30<br>Fax: (86) 0769-55501234<br>Email: info@veltrano.se
</address>
<div class="abs footer-col" style="left:413px;top:2144px">
  <h4>Our Services</h4>
  Accounting<br>Payroll Management<br>Annual Accounts &amp; Declarations<br>Project Accounting<br>Financial Management<br>Finance Department
</div>
<div class="abs footer-col" style="left:736px;top:2144px">
  <h4>Company</h4>
  About Us<br>Contact Us<br>Resources<br>Guidance
</div>
<p class="abs member">Member of Nordic Guild of<br>Bookkeeping Advisers</p>
<div class="abs member-badge" role="img" aria-label="Membership badge"></div>

<div class="abs footer-bottom"></div>
<p class="abs copyright">Copyright © 2020 Veltrano AB. All rights reserved.</p>
<p class="abs legal">Privacy Policy | Terms &amp; Conditions</p>
<div class="abs accent-strip"></div>

</body>
</html>
```